The Plaster & Resonance Craftworks Inc (PRCI)

Create a LOGO and Business Card design.

Colors: Black, Bright Yellow & Red

Description of company: commercial carpentry, metal framing, drywall, taping/spackling, demolition, rough/finish carpentry.

Target Market(s)

developers, architects, general contractors, construction managers

Industry/Entity Type

Business

```html
<!DOCTYPE html>
<html lang="en">
<head>
<meta charset="utf-8">
<title>PRCI Business Card</title>
<link rel="stylesheet" href="https://fonts.googleapis.com/css2?family=Arimo:wght@400;700&display=swap">
<style>
  :root {
    --backdrop: #000000;
    --card: #ffffff;
    --card-edge: #111111;
    --leaf: #ffd600;
    --accent: #e0201b;
    --ink: #111111;
    --contact: #222222;
  }
  * { box-sizing: border-box; margin: 0; padding: 0; }
  html, body {
    width: 1200px; height: 906px; overflow: hidden;
    background: var(--backdrop);
    font-family: "Arimo", Arial, sans-serif;
  }
  .canvas { position: relative; width: 1200px; height: 906px; }
  .card {
    position: absolute; left: 185px; top: 190px;
    width: 833px; height: 473px;
    background: var(--card);
    border: 3px solid var(--card-edge);
    overflow: hidden;
  }
  .card__leaf { position: absolute; inset: 0; width: 100%; height: 100%; }
  .brand {
    position: absolute; left: 30px; top: 34px;
    display: flex; align-items: center; gap: 12px;
  }
  .brand__square {
    width: 30px; height: 30px;
    background: var(--accent);
  }
  .brand__name {
    font-size: 50px; font-weight: 700; color: var(--ink);
    line-height: 1; letter-spacing: 1px;
  }
  .brand__tagline {
    position: absolute; left: 22px; top: 124px;
    font-size: 15px; color: var(--ink);
  }
  .person {
    position: absolute; left: 300px; top: 196px;
    text-align: right;
  }
  .person__name {
    font-size: 44px; color: var(--ink); line-height: 1;
  }
  .person__name strong { font-weight: 700; }
  .person__role {
    font-size: 20px; color: var(--accent); margin-top: 4px;
  }
  .contact {
    position: absolute; left: 606px; top: 298px;
    height: 162px; padding-left: 14px;
    border-left: 2px solid var(--accent);
    font-size: 17px; line-height: 18.5px; color: var(--contact);
    font-style: normal;
  }
  .contact__row { display: flex; }
  .contact__label { width: 26px; flex: none; color: var(--accent); font-weight: 700; }
</style>
</head>
<body>
<main class="canvas">
  <section class="card">
    <svg class="card__leaf" viewBox="0 0 833 473" preserveAspectRatio="none" aria-hidden="true">
      <path d="M18,468 C110,230 430,50 830,6 C780,210 560,420 18,468 Z" fill="var(--leaf)"/>
    </svg>

    <div class="brand">
      <span class="brand__square"></span>
      <span class="brand__name">PRCI</span>
    </div>
    <p class="brand__tagline">The Plaster &amp; Resonance Craftworks Inc</p>

    <div class="person">
      <p class="person__name"><strong>Lena</strong> Marsh</p>
      <p class="person__role">Director</p>
    </div>

    <address class="contact">
      <div class="contact__row"><span class="contact__label">A:</span><span>Level 6,<br>18 Ferrow Lane,<br>Carlow Heights 2041<br>NSW Australia</span></div>
      <div class="contact__row"><span class="contact__label">P:</span><span>041598765432</span></div>
      <div class="contact__row"><span class="contact__label">E:</span><span>hello@prcimail.com</span></div>
      <div class="contact__row"><span class="contact__label">W:</span><span>www.prci-works.com</span></div>
    </address>
  </section>
</main>
</body>
</html>
```